Business Card Design for Fashion Tech Startup

Dear designers, we need a business card for Asia's premier fashion tech startup.!

PebbleHop is discovery e-commerce destination for busy, discerning parents in Asia featuring leading independent designers of baby, kids fashion apparel and sustainable brands from around the world.

PebbleHop is a modern, contemporary fashion tech startup targeting well-educated, well travelled and affluent parents. We're NOT your typical kiddy store!! Our design philosophy & e-commerce site is more like Vask.com, Orimesa.com, Pondwick.com, Farthollow.com.
Updates

Hi, size of the business card should be 84mm X 55mm. Would appreciate some business card layouts in Portrait as added consideration, i fancy the idea of a Portrait business card. What's important is that the business card should pique the receiver's interest to log onto the website to learn more. Many thanks and love forward to the designs!

Target Market(s)

Though modern, classy in look, feel & positioning, PebbleHop does possess a cheeky, fun-loving personality as depicted by its logo and the segment it targets (baby, kids) though the key decision makers i.e primarily mums between 25-40 who are well educated/travelled, local & expatriates, internet/digitally savvy, mid-high income working mums.

Industry/Entity Type

E-Commerce

Requirements
Must have
• Name, designation, email, phone & mobile number.
Company url : www.pebblehop.sg
Slogan : Discovery e-commerce destination for discerning, busy parents
Nice to have
• Call to Action such as a Discount code offering 10% discount
or asking people to "Like" us on our Chatterly page/Chatterly URL

```html
<!DOCTYPE html>
<html lang="en">
<head>
<meta charset="utf-8">
<title>PebbleHop Business Card</title>
<link href="https://fonts.googleapis.com/css2?family=Open+Sans:wght@400;600;700&display=swap" rel="stylesheet">
<style>
  :root {
    --navy: #355a6e;
    --coral: #f3806a;
    --ink: #4a4f55;
    --paper: #ffffff;
    --backdrop: #e9eaee;
  }
  * { margin: 0; padding: 0; box-sizing: border-box; }
  html, body { width: 1200px; height: 987px; overflow: hidden; background: var(--backdrop); }
  body { font-family: "Open Sans", Arial, sans-serif; position: relative; }

  .card {
    position: absolute;
    left: 260px;
    width: 680px;
    height: 445px;
    background: var(--paper);
    border-radius: 34px;
    overflow: hidden;
    box-shadow: 0 6px 18px rgba(40, 50, 70, 0.18);
  }
  .card--brand { top: 34px; }
  .card--contact { top: 508px; }

  /* Brand side */
  .brand-lockup {
    position: absolute;
    left: 0; right: 0; top: 140px;
    display: flex; align-items: center; justify-content: center; gap: 22px;
  }
  .brand-dot {
    width: 92px; height: 92px; border-radius: 50%;
    background: var(--coral);
  }
  .brand-name {
    font-weight: 700; font-size: 70px; color: var(--navy); letter-spacing: 1px;
  }
  .social-line {
    position: absolute; left: 0; right: 0; top: 300px;
    display: flex; justify-content: center; align-items: center; gap: 10px;
    font-size: 24px; color: var(--ink);
  }
  .social-line .network { color: var(--navy); font-weight: 600; }

  /* Contact side */
  .accent-tab {
    position: absolute; left: 26px; top: 26px; width: 12px; height: 52px; background: var(--navy);
  }
  .person { position: absolute; left: 56px; top: 24px; }
  .person__name { font-size: 26px; font-weight: 600; color: var(--coral); line-height: 1.1; }
  .person__title { font-size: 15px; color: var(--navy); }
  .slogan {
    position: absolute; left: 56px; top: 96px; width: 300px;
    font-size: 21px; line-height: 1.25; color: var(--ink);
  }
  .contacts { position: absolute; left: 56px; top: 192px; list-style: none; font-size: 18px; color: var(--ink); }
  .contacts li { display: flex; align-items: center; gap: 10px; height: 27px; }
  .contacts svg { width: 18px; height: 18px; fill: var(--navy); }
  .contacts .plain { padding-left: 0; }

  .bands { position: absolute; left: 0; bottom: 0; width: 680px; height: 445px; }
  .band-url {
    position: absolute; left: 56px; top: 331px;
    font-size: 20px; color: var(--paper); letter-spacing: 0.5px;
  }
  .emblem {
    position: absolute; right: 60px; top: 60px; width: 250px; height: 250px; border-radius: 50%;
    background: radial-gradient(circle at 50% 45%, var(--navy) 0 22%, var(--coral) 23% 60%, #e8957f 61% 100%);
  }
</style>
</head>
<body>

  <section class="card card--brand">
    <div class="brand-lockup">
      <span class="brand-dot"></span>
      <span class="brand-name">PebbleHop</span>
    </div>
    <p class="social-line"><span class="network">Chatterly</span><span>/pebblehop</span></p>
  </section>

  <section class="card card--contact">
    <span class="accent-tab"></span>
    <div class="person">
      <p class="person__name">Your Name</p>
      <p class="person__title">Title</p>
    </div>
    <p class="slogan">Discovery e-commerce destination for discerning busy parents</p>
    <ul class="contacts">
      <li>
        <svg viewBox="0 0 24 24" aria-hidden="true"><circle cx="12" cy="12" r="11" fill="none" stroke="#355a6e" stroke-width="2"/><path d="M8 6l2 0 1 3-1.5 1a7 7 0 0 0 3.5 3.5L14 12l3 1v2c0 1-1 2-2 2A9 9 0 0 1 7 9c0-1 0-3 1-3z"/></svg>
        012-345-6789
      </li>
      <li>
        <svg viewBox="0 0 24 24" aria-hidden="true"><rect x="7" y="2" width="10" height="20" rx="2"/><rect x="9" y="5" width="6" height="9" fill="#fff"/></svg>
        012-345-6789
      </li>
      <li>
        <svg viewBox="0 0 24 24" aria-hidden="true"><rect x="2" y="5" width="20" height="14" rx="2"/><path d="M3 6l9 7 9-7" fill="none" stroke="#fff" stroke-width="2"/></svg>
        info@pebblehop.com
      </li>
      <li class="plain">www.pebblehop.com</li>
    </ul>

    <svg class="bands" viewBox="0 0 680 445" aria-hidden="true">
      <path d="M0 312 H400 C440 312 450 350 490 350 H680 V445 H0 Z" fill="#355a6e"/>
      <path d="M0 372 H420 C455 372 460 352 495 352 H680 V445 H0 Z" fill="#f3806a"/>
    </svg>
    <p class="band-url">www.pebblehop.asia</p>

    <div class="emblem" role="img" aria-label="Round emblem of baby and kids items around the PebbleHop.sg name"></div>
  </section>

</body>
</html>
```